載内容詳細に関しては、別添のExcel資料を参照してください。

・ターゲット
BtoB
木工架装を出来る業者を探している車のリース販売会社の担当様

・カラーイメージ
木目デザインと企業カラーである紺色を使用してデザインお願いします
▼木目参考
https://www.tomika-kobo.jp/
▼紺参考
https://www.rvm-t.jp/

・デザイン、ムード
木を扱う仕事なので、木目を上手く使ってデザインしてほしい
▼参考

・JQについて
JQのパターン制作は不要です。
1枚目の画像でデザインお願いします

配置やデザイン等はアレンジしていただいて構いません。
また、縦に制限はありません。

レスポンシブデザインのサイトで、bootstrap4を利用しコーディングする予定になります。

デザイン幅は2000px、コンテンツの幅はbootstrap4デフォルトのの1110pxを基準としてください。
ただし、最近のデザインの流行を取りいれて、フルワイドや、1200~15000px程度の幅のコンテンツをバランスよくレイアウトしてください。
コンテンツ配置は基本12分割になります。がデザインによっては、多少逸脱してもかまいません。
bootstrap4、12分割グリッドの基準のPSDも資料として添付しております。
ご参考になさってください。

本分のフォントはゴシック系は游ゴシック、メイリオ、明朝系は遊明朝でお願いします。
飾り文字はフリーフォントか、googleフォントを利用してください。

メイン画像部分・グローバルメニューは、ワイド適用でお願いします。

不明点、質問などありましたらメッセージ等でご連絡ください。
1ページ
青系、水色系
• 高解像度JPG (.jpg)
• フォトショップ形式 (.psd)
・資料上はサイト名(社名)や住所などは伏字にしております。
ご提案時点ではそのまま作成をお願いします。

・使用画像は当選後こちらで用意します。
ご提案時点では前項同様に、カンプデータ等をご使用のうえ、当選後に本内容へ差し替え修正をお願いします。
また、雰囲気が合っていれば、指定外の画像を追加掲載いただいてOKです。

・当選前提となった方は正式な社名及び連絡先をお伝えしますので修正対応をお願いします。
また希望の際は、当選後、中ページの制作及びコーディングも別途ご依頼可能です。

```html
<!DOCTYPE html>
<html lang="ja">
<head>
<meta charset="utf-8">
<title>木工架装施工専門業者 〇〇〇〇</title>
<link rel="stylesheet" href="https://fonts.googleapis.com/css2?family=Noto+Sans+JP:wght@400;500;700&family=Noto+Serif+JP:wght@500;700&family=Roboto:wght@500;700;900&display=swap">
<style>
:root{
  --navy:#1c3579;
  --navy-dark:#132658;
  --beige:#f3f0ea;
  --ink:#333;
  --muted:#666;
  --white:#fff;
  --wood-light:#c98a56;
  --wood-mid:#a8623a;
  --wood-dark:#6e3c22;
}
*{margin:0;padding:0;box-sizing:border-box}
html,body{width:1200px;height:2292px;overflow:hidden}
body{font-family:"Noto Sans JP",sans-serif;color:var(--ink);background:var(--white);position:relative}
.site-header{height:56px;display:flex;align-items:center;justify-content:space-between;padding:0 24px;background:var(--white)}
.brand{display:flex;align-items:center;gap:10px}
.brand-lead{font-size:9px;color:var(--muted);line-height:1.3}
.brand-name{font-size:14px;font-weight:700;color:var(--ink)}
.brand-mark{width:24px;height:24px;background:var(--navy)}
.header-right{text-align:right}
.header-contact{display:flex;gap:12px;justify-content:flex-end;align-items:center;font-size:13px;color:var(--navy);font-weight:700}
.header-mail{background:var(--navy);color:var(--white);font-size:10px;padding:4px 12px}
.global-nav{display:flex;gap:26px;justify-content:flex-end;font-size:10px;color:var(--ink);margin-top:6px}
.hero{position:relative;height:452px;overflow:hidden}
.hero-photo{position:absolute;inset:0;background:radial-gradient(ellipse at 50% 60%,#c8743f 0%,#a85a30 40%,#5a3325 75%,#2a2a2f 100%)}
.hero-copy{position:absolute;top:70px;left:0;right:0;text-align:center;color:var(--white);font-family:"Noto Serif JP",serif}
.hero-title{font-size:30px;font-weight:700;letter-spacing:3px;text-shadow:0 2px 8px rgba(0,0,0,.4)}
.hero-sub{font-size:17px;margin-top:44px;line-height:1.7;text-shadow:0 2px 6px rgba(0,0,0,.4)}
.hero-watermark{position:absolute;left:0;right:0;bottom:-6px;text-align:center;font-family:"Roboto",sans-serif;font-weight:900;font-size:80px;color:rgba(255,255,255,.35);letter-spacing:2px;line-height:1;white-space:nowrap}
.intro{height:312px;text-align:center;padding-top:64px}
.intro-title{font-family:"Noto Serif JP",serif;font-size:22px;font-weight:700;color:var(--ink)}
.intro-sub{font-family:"Noto Serif JP",serif;font-size:15px;margin-top:10px}
.intro-text{font-size:12px;line-height:2.2;margin-top:22px;color:var(--ink)}
.section{position:relative;text-align:center}
.section-beige{background:var(--beige)}
.section-head{position:relative;height:120px;padding-top:40px}
.section-title{position:relative;font-family:"Roboto",sans-serif;font-weight:700;font-size:36px;color:var(--navy);letter-spacing:2px;z-index:1;line-height:1.2}
.section-sub{position:relative;font-size:11px;color:var(--ink);z-index:1;margin-top:2px}
.section-ghost{position:absolute;top:66px;left:0;right:0;font-family:"Roboto",sans-serif;font-weight:900;font-size:64px;color:rgba(28,53,121,.06);letter-spacing:4px;line-height:1;z-index:0}
.business{height:440px}
.business-body{position:absolute;top:200px;left:268px;width:664px;height:200px;display:flex}
.business-card{width:268px;background:var(--white);text-align:left;padding:30px 28px;margin-top:12px;height:168px}
.business-card p{font-size:10px;line-height:1.9;color:var(--ink)}
.btn{display:inline-block;background:var(--navy);color:var(--white);font-size:10px;padding:6px 22px}
.business-card .btn{margin-top:14px}
.business-photo{flex:1;background:linear-gradient(135deg,#b0633a,#8a4526 50%,#c07a4a)}
.works{height:412px}
.works-gallery{position:absolute;top:148px;left:260px;width:680px;height:148px;display:flex;gap:8px}
.works-gallery div{flex:1}
.works .btn{position:absolute;top:336px;left:552px;width:96px;padding:6px 0}
.contact{height:448px}
.contact-body{position:absolute;top:160px;left:264px;width:668px;height:216px;display:flex}
.contact-photo{width:336px;background:linear-gradient(135deg,#cfc5b6,#8d7f70 50%,#b9a68f)}
.contact-panel{flex:1;background:var(--navy);padding:28px 34px;color:var(--white);text-align:left}
.contact-panel p{font-size:10px;line-height:1.8;text-align:center}
.contact-btn{display:flex;align-items:center;justify-content:center;gap:8px;background:var(--white);color:var(--navy);font-size:12px;font-weight:700;height:34px;margin:14px auto 0;width:170px}
.site-footer{position:absolute;top:2120px;left:0;width:1200px;height:152px;background:linear-gradient(180deg,var(--wood-light),var(--wood-mid) 40%,var(--wood-light) 70%,var(--wood-dark));color:var(--white)}
.footer-info{position:absolute;left:264px;top:40px;font-size:10px;line-height:1.8}
.footer-nav{position:absolute;right:268px;top:40px;display:flex;gap:28px;font-size:10px}
.page-top{position:absolute;left:585px;top:112px;width:30px;height:30px;background:var(--navy);display:flex;align-items:center;justify-content:center}
.copyright{position:absolute;top:2272px;left:0;width:1200px;height:20px;background:var(--navy-dark);color:var(--white);font-size:8px;text-align:center;line-height:20px}
</style>
</head>
<body>
<header class="site-header">
  <div class="brand">
    <div>
      <div class="brand-lead">車内木工架装施工専門業者</div>
      <div class="brand-name">〇〇〇〇</div>
    </div>
    <div class="brand-mark"></div>
  </div>
  <div class="header-right">
    <div class="header-contact">
      <span>
        <svg width="11" height="11" viewBox="0 0 24 24" fill="currentColor"><path d="M6.6 10.8a15 15 0 006.6 6.6l2.2-2.2a1 1 0 011-.25 11.4 11.4 0 003.6.57 1 1 0 011 1V20a1 1 0 01-1 1A17 17 0 013 4a1 1 0 011-1h3.5a1 1 0 011 1c0 1.25.2 2.45.57 3.6a1 1 0 01-.25 1z"/></svg>
        Tel.000-0000-0000
      </span>
      <span class="header-mail">お問い合わせ</span>
    </div>
    <nav class="global-nav"><span>HOME</span><span>事業紹介</span><span>施工事例</span><span>会社概要</span><span>お問い合わせ</span></nav>
  </div>
</header>

<section class="hero">
  <div class="hero-photo" role="img" aria-label="木工架装を施したワンボックス車の荷室内部の写真"></div>
  <div class="hero-copy">
    <h1 class="hero-title">木工架装施工専門業者〇〇〇〇</h1>
    <p class="hero-sub">その細かいこだわりと<br>お客様のご要望を叶える確かな技術</p>
  </div>
  <div class="hero-watermark">〇〇〇〇 WOODWORKING</div>
</section>

<section class="intro">
  <h2 class="intro-title">車内の木工架装工事なら〇〇〇〇にご相談ください！</h2>
  <p class="intro-sub">「安心・確実」な木製の工程で、確かな技術でお応えします。</p>
  <p class="intro-text">
    木工架装専門業者〇〇〇〇は、自動車リース会社様の車両に木製の内装を施工しております。<br>
    床張りや棚の設置など、用途に合わせた架装をご提案し、丁寧に仕上げてまいります。<br>
    長年の経験で培った技術により、耐久性と使いやすさを両立した施工をお約束します。<br>
    車種やご予算に応じて柔軟に対応いたしますので、まずはお気軽にご相談ください。<br>
    少数の車両から大量のご依頼まで、迅速に対応いたします。
  </p>
</section>

<section class="section section-beige business">
  <div class="section-head">
    <div class="section-ghost">BUSINESS</div>
    <h2 class="section-title">BUSINESS</h2>
    <p class="section-sub">事業紹介</p>
  </div>
  <div class="business-body">
    <div class="business-card">
      <p>車両の床張りや荷室棚の製作など、木工架装の施工を行っております。ご要望に合わせた設計から仕上げまで一貫して対応いたします。</p>
      <span class="btn">詳細を見る</span>
    </div>
    <div class="business-photo" role="img" aria-label="木製フローリングを施工した荷室の写真"></div>
  </div>
</section>

<section class="section works">
  <div class="section-head">
    <div class="section-ghost">WORKS</div>
    <h2 class="section-title">WORKS</h2>
    <p class="section-sub">施工事例</p>
  </div>
  <div class="works-gallery">
    <div role="img" aria-label="施工事例：木製棚を設置した車内の写真" style="background:linear-gradient(135deg,#d9a26c,#9b5a33)"></div>
    <div role="img" aria-label="施工事例：車両外観と荷室の写真" style="background:linear-gradient(135deg,#9a8c80,#5b4a40)"></div>
    <div role="img" aria-label="施工事例：木製の床と内張りの写真" style="background:linear-gradient(135deg,#c27a45,#7a3f22)"></div>
    <div role="img" aria-label="施工事例：荷室全面の木工架装の写真" style="background:linear-gradient(135deg,#d08a55,#8a4a2a)"></div>
  </div>
  <span class="btn">もっと見る</span>
</section>

<section class="section section-beige contact">
  <div class="section-head">
    <div class="section-ghost">CONTACT</div>
    <h2 class="section-title">CONTACT</h2>
    <p class="section-sub">お問い合わせ</p>
  </div>
  <div class="contact-body">
    <div class="contact-photo" role="img" aria-label="木材を加工する作業風景の写真"></div>
    <div class="contact-panel">
      <p>ご依頼、ご相談はお電話またはメールフォームよりお気軽にどうぞ</p>
      <div class="contact-btn">
        <svg width="14" height="14" viewBox="0 0 24 24" fill="currentColor"><path d="M6.6 10.8a15 15 0 006.6 6.6l2.2-2.2a1 1 0 011-.25 11.4 11.4 0 003.6.57 1 1 0 011 1V20a1 1 0 01-1 1A17 17 0 013 4a1 1 0 011-1h3.5a1 1 0 011 1c0 1.25.2 2.45.57 3.6a1 1 0 01-.25 1z"/></svg>
        000-0000-0000
      </div>
      <div class="contact-btn">
        <svg width="14" height="14" viewBox="0 0 24 24" fill="none" stroke="currentColor" stroke-width="2"><rect x="3" y="5" width="18" height="14"/><path d="M3 6l9 7 9-7"/></svg>
        お問い合わせ
      </div>
    </div>
  </div>
</section>

<footer class="site-footer" role="img" aria-label="木目の背景">
  <div class="footer-info">
    車内木工架装施工専門業者〇〇〇〇<br>
    〒000-0000 〇〇県〇〇市〇〇町0-0-0<br>
    TEL 000-0000-0000 / FAX 000-0000-0000
  </div>
  <nav class="footer-nav"><span>HOME</span><span>事業紹介</span><span>施工事例</span><span>お問い合わせ</span></nav>
  <div class="page-top">
    <svg width="12" height="12" viewBox="0 0 24 24" fill="none" stroke="#fff" stroke-width="3"><path d="M5 15l7-7 7 7"/></svg>
  </div>
</footer>
<div class="copyright">Copyright © 〇〇〇〇 All Rights Reserved.</div>
</body>
</html>
```